" As soluçoes oferecidas pela Kalvira atendem às exigências legais e se adequam as necessidades de cada cliente. Dessa forma, respeitando as necessidades específicas e buscando a otimizaçao e aumento de eficiência das rotinas, os produtos fornecidos formam o núcleo básico integrado de soluçao mais inteligente em Gestao da Administraçao do mercado. Com nossas ferramentas de controle da integrada, buscamos oferecer aos nossos clientes a melhoria no planejamento e consequentemente a garantia de um serviço de qualidade ao cidadao. Para garantirmos o atendimento ao número crescente de clientes, contamos com uma equipe qualificada, profissionais com experiência na Gestao Publica Municipal e principalmente com a busca pela inovaçao. Mais do que um produto em software, oferecemos a melhor soluçao do mercado para a Gestao Municipal, oferecendo as melhores práticas adotadas e total aderência a conceitos legais "

```html
<!DOCTYPE html>
<html lang="pt-BR">
<head>
<meta charset="UTF-8">
<title>Kalvira Tecnologia – Cartão de Visita</title>
<link href="https://fonts.googleapis.com/css2?family=Questrial&display=swap" rel="stylesheet">
<style>
  :root {
    --stage: #2b2b2b;
    --card-white: #ffffff;
    --card-white-shade: #eef0ee;
    --green-deep: #1c3522;
    --green-dark: #2c4a32;
    --green-bright: #8cc63f;
    --green-soft: #b9dc7a;
    --text-light: #f2f5f0;
    --text-dark: #4a4f4a;
    --icon-box: #8a9a86;
  }
  * { margin: 0; padding: 0; box-sizing: border-box; }
  html, body {
    width: 1200px; height: 1200px; overflow: hidden;
    background: var(--stage);
    font-family: "Questrial", sans-serif;
  }
  .canvas {
    width: 1200px; height: 1200px;
    display: flex; flex-direction: column;
    align-items: center; justify-content: center; gap: 56px;
  }
  .card {
    width: 900px; height: 514px; position: relative; overflow: hidden;
    box-shadow: 0 18px 40px rgba(0,0,0,.45);
  }
  .card--front {
    background: linear-gradient(120deg, var(--card-white) 55%, var(--card-white-shade));
  }
  .card--back {
    background: linear-gradient(135deg, var(--green-dark), var(--green-deep));
  }
  .brand {
    position: absolute; display: flex; align-items: center; gap: 22px;
  }
  .brand__dot { border-radius: 50%; background: var(--green-bright); flex: none; }
  .brand__name { line-height: 1; letter-spacing: 1px; }
  .card--front .brand { left: 90px; top: 205px; }
  .card--front .brand__dot { width: 96px; height: 96px; }
  .card--front .brand__name { font-size: 92px; color: var(--text-dark); }
  .card--back .brand { right: 120px; top: 70px; }
  .card--back .brand__dot { width: 64px; height: 64px; }
  .card--back .brand__name { font-size: 62px; color: var(--text-light); }
  .contact {
    position: absolute; left: 70px; top: 250px;
    list-style: none; display: flex; flex-direction: column; gap: 18px;
  }
  .contact__item {
    display: flex; align-items: flex-start; gap: 18px;
    color: var(--text-light); font-size: 29px; line-height: 1.15;
  }
  .contact__icon {
    width: 38px; height: 38px; flex: none; border-radius: 4px;
    background: var(--icon-box); display: flex; align-items: center; justify-content: center;
  }
  .contact__icon svg { width: 26px; height: 26px; }
</style>
</head>
<body>
<main class="canvas">
  <section class="card card--front" aria-label="Frente do cartão">
    <div class="brand">
      <span class="brand__dot"></span>
      <span class="brand__name">Kalvira</span>
    </div>
  </section>

  <section class="card card--back" aria-label="Verso do cartão">
    <div class="brand">
      <span class="brand__dot"></span>
      <span class="brand__name">Kalvira</span>
    </div>
    <ul class="contact">
      <li class="contact__item">
        <span class="contact__icon">
          <svg viewBox="0 0 24 24" fill="none" stroke="#fff" stroke-width="2"><rect x="7" y="2" width="10" height="20" rx="2"/><line x1="10" y1="18" x2="14" y2="18"/></svg>
        </span>
        <span>11 - 4820 3157</span>
      </li>
      <li class="contact__item">
        <span class="contact__icon">
          <svg viewBox="0 0 24 24" fill="none" stroke="#fff" stroke-width="2"><circle cx="12" cy="12" r="4"/><path d="M16 8v5a3 3 0 0 0 6 0v-1a10 10 0 1 0-4 8"/></svg>
        </span>
        <span>www.kalvira.com.br</span>
      </li>
      <li class="contact__item">
        <span class="contact__icon">
          <svg viewBox="0 0 24 24" fill="none" stroke="#fff" stroke-width="2"><rect x="3" y="5" width="18" height="14" rx="1"/><path d="M3 6l9 7 9-7"/></svg>
        </span>
        <span>contato@kalvira.com.br</span>
      </li>
      <li class="contact__item">
        <span class="contact__icon">
          <svg viewBox="0 0 24 24" fill="none" stroke="#fff" stroke-width="2"><path d="M12 22s7-7 7-12a7 7 0 0 0-14 0c0 5 7 12 7 12z"/><circle cx="12" cy="10" r="2.5"/></svg>
        </span>
        <span>Rua das Palmeiras, 412<br>Centro - Sao Paulo SP</span>
      </li>
    </ul>
  </section>
</main>
</body>
</html>
```